Business card design needed for a security services business.

We provide a wide range of security services from guard personnel to electronic systems.

Industry/Entity Type

Security Industry

Contact Information for Business Card

Brent Holloway, Owner Office: 780.555.0148; Cell: 780.555.0193 Email: brent@norcrestwatchgroup.example; Address 20487 163 St Edmonton, AB T5X 2K8

Colors
0054AA
0677BA
7BADD7
CADEEF
E8F1F8

Requirements
Nice to have
• On the back of the card I would like to possible list the services I provide: Guards Mobiles Live Video Surveillance Access Intrusion

```html
<!DOCTYPE html>
<html lang="en">
<head>
<meta charset="utf-8">
<title>Norcrest Watch Group – Business Card</title>
<link rel="stylesheet" href="https://fonts.googleapis.com/css2?family=Lato:wght@400;700;900&display=swap">
<style>
  :root {
    --bg: #e9ebee;
    --card-dark: #1b1b1c;
    --card-light: #ffffff;
    --blue: #0677ba;
    --blue-deep: #0054aa;
    --grey: #6d6e70;
    --grey-light: #9a9b9d;
    --text-dark: #333436;
    --white: #ffffff;
  }
  * { margin: 0; padding: 0; box-sizing: border-box; }
  html, body { width: 1200px; height: 801px; overflow: hidden; }
  body {
    background: var(--bg);
    font-family: "Lato", Arial, sans-serif;
    display: flex;
    align-items: center;
    justify-content: center;
    gap: 40px;
  }
  .card {
    position: relative;
    width: 540px;
    height: 309px;
    border-radius: 18px;
    overflow: hidden;
    box-shadow: 0 6px 18px rgba(0,0,0,0.18);
  }

  /* Front */
  .card--front {
    background: var(--card-dark);
    color: var(--white);
  }
  .brand {
    position: absolute;
    left: 0; right: 0; top: 80px;
    text-align: center;
  }
  .brand__name {
    font-weight: 900;
    font-size: 30px;
    letter-spacing: 1px;
    color: var(--blue);
    line-height: 1.1;
    white-space: nowrap;
  }
  .brand__rule {
    width: 380px;
    height: 2px;
    background: var(--grey);
    margin: 22px auto 0;
  }
  .services {
    position: absolute;
    left: 0; right: 0; top: 190px;
    text-align: center;
    font-size: 15px;
    line-height: 1.55;
    color: var(--white);
  }
  .services .dot { color: var(--blue); padding: 0 4px; }

  /* Back */
  .card--back { background: var(--card-light); }
  .person {
    position: absolute;
    left: 16px; top: 104px;
    width: 230px;
    text-align: right;
  }
  .person__name {
    font-weight: 900;
    font-size: 22px;
    color: var(--blue);
    letter-spacing: -0.3px;
    line-height: 1.1;
    white-space: nowrap;
  }
  .person__title {
    font-size: 16px;
    color: var(--grey);
    margin-top: 2px;
  }
  .divider {
    position: absolute;
    left: 262px; top: 78px;
    width: 1px; height: 98px;
    background: var(--grey-light);
  }
  .contacts {
    position: absolute;
    left: 276px; top: 78px;
    list-style: none;
    font-size: 12.5px;
    color: var(--text-dark);
    white-space: nowrap;
  }
  .contacts li {
    display: flex;
    align-items: center;
    gap: 8px;
    height: 24.5px;
  }
  .contacts svg { width: 12px; height: 12px; flex: none; fill: var(--blue); }
  .contacts .phone-num { font-size: 15px; }
  .band {
    position: absolute;
    left: 0; bottom: 44px;
    width: 400px; height: 34px;
    background: var(--blue);
    display: flex;
    align-items: center;
    padding-left: 70px;
    color: var(--white);
    font-size: 15px;
    gap: 7px;
    white-space: nowrap;
  }
  .band svg { width: 12px; height: 15px; fill: var(--white); }
  .mark {
    position: absolute;
    right: 20px; bottom: 52px;
    display: flex;
    align-items: center;
    gap: 8px;
  }
  .mark__name {
    font-weight: 900;
    font-size: 16px;
    color: var(--blue);
    white-space: nowrap;
  }
  .mark__square {
    width: 16px; height: 16px;
    background: var(--grey);
  }
</style>
</head>
<body>

  <section class="card card--front">
    <div class="brand">
      <div class="brand__name">NORCREST WATCH GROUP</div>
      <div class="brand__rule"></div>
    </div>
    <p class="services">
      Card Access Systems<span class="dot">•</span>Mobile Patrols<br>
      Security guards<span class="dot">•</span>Video Surveillance Systems
    </p>
  </section>

  <section class="card card--back">
    <div class="person">
      <h1 class="person__name">BRENT HOLLOWAY</h1>
      <p class="person__title">Owner</p>
    </div>
    <div class="divider"></div>
    <ul class="contacts">
      <li class="phone-num">
        <svg viewBox="0 0 24 24"><path d="M6.6 10.8c1.4 2.8 3.8 5.1 6.6 6.6l2.2-2.2c.3-.3.7-.4 1-.2 1.1.4 2.3.6 3.6.6.6 0 1 .4 1 1V20c0 .6-.4 1-1 1C10.6 21 3 13.4 3 4c0-.6.4-1 1-1h3.5c.6 0 1 .4 1 1 0 1.3.2 2.5.6 3.6.1.3 0 .7-.2 1l-2.3 2.2z"/></svg>
        780.555.0148
      </li>
      <li class="phone-num">
        <svg viewBox="0 0 24 24"><path d="M7 1h10c1.1 0 2 .9 2 2v18c0 1.1-.9 2-2 2H7c-1.1 0-2-.9-2-2V3c0-1.1.9-2 2-2zm0 3v14h10V4H7zm5 15.5a1 1 0 1 0 0 2 1 1 0 0 0 0-2z"/></svg>
        780.555.0193
      </li>
      <li>
        <svg viewBox="0 0 24 24"><path d="M2 5h20v14H2V5zm2 2v.5l8 5 8-5V7H4zm0 2.8V17h16V9.8l-8 5-8-5z"/></svg>
        brent@norcrestwatchgroup.example
      </li>
      <li>
        <svg viewBox="0 0 24 24"><path d="M12 2a10 10 0 1 0 0 20 10 10 0 0 0 0-20zm6.9 9h-3c-.1-2.4-.6-4.5-1.4-6A8 8 0 0 1 18.9 11zM12 4c.9 1.2 1.8 3.6 1.9 7h-3.8c.1-3.4 1-5.8 1.9-7zM9.5 5c-.8 1.5-1.3 3.6-1.4 6h-3A8 8 0 0 1 9.5 5zM5.1 13h3c.1 2.4.6 4.5 1.4 6A8 8 0 0 1 5.1 13zM12 20c-.9-1.2-1.8-3.6-1.9-7h3.8c-.1 3.4-1 5.8-1.9 7zm2.5-1c.8-1.5 1.3-3.6 1.4-6h3a8 8 0 0 1-4.4 6z"/></svg>
        norcrestwatchgroup.example
      </li>
    </ul>

    <div class="band">
      <svg viewBox="0 0 16 20"><path d="M8 0a7 7 0 0 0-7 7c0 5 7 13 7 13s7-8 7-13a7 7 0 0 0-7-7zm0 10a3 3 0 1 1 0-6 3 3 0 0 1 0 6z"/></svg>
      20487 163 St Edmonton, AB T5X 2K8
    </div>
    <div class="mark">
      <span class="mark__name">NORCREST</span>
      <span class="mark__square"></span>
    </div>
  </section>

</body>
</html>
```